Redesign BrightCoinDesk.info

We are unhappy with the design and layout of our current site www.BrightCoinDesk.info
We would like the following pages redesigned using a consistent style.
http://www.brightcoindesk.info/
http://www.brightcoindesk.info/live_forex_signals.php
http://www.brightcoindesk.info/forex-signal/71/TQ-Overdrive.html
http://www.brightcoindesk.info/broker_rebates.php
http://www.brightcoindesk.info/contact.php
Ideally we would also like the contractor to be able to code it into HTML.
We currently like our colour scheme of black, blue and grey.
Updates
We would like to consider a logo redesign. We're happy to pay a $30 bonus for a new logo.
Target Market(s)
80% males between 25 and 50 years old
Industry/Entity Type
Contractor

```html
<!DOCTYPE html>
<html lang="en">
<head>
<meta charset="utf-8">
<title>BrightCoinDesk.info</title>
<link href="https://fonts.googleapis.com/css2?family=Arimo:ital,wght@0,400;0,700;1,400&family=Noto+Serif:ital,wght@1,400&display=swap" rel="stylesheet">
<style>
:root{
  --blue:#1f9fe0;
  --blue-dark:#137cc0;
  --red:#d8141c;
  --orange:#f47a1f;
  --ink:#111;
  --text:#555;
  --grey-band:#7a7a7a;
  --dark-band:#333;
  --footer:#222;
  --page:#f3f3f3;
  --topbar:#ececec;
  --link:#1a8fd0;
}
*{box-sizing:border-box;margin:0;padding:0}
html,body{width:680px;height:1200px;overflow:hidden}
body{position:relative;background:#fff;font-family:"Arimo",Arial,sans-serif;color:var(--text)}
.abs{position:absolute}

.topbar{left:0;top:0;width:680px;height:20px;background:var(--topbar);font-size:7px;color:#555}
.topbar .item{top:5px;display:flex;align-items:center;gap:6px;white-space:nowrap;line-height:10px}
.topbar .addr{left:74px}
.topbar .phone{left:229px}
.search{left:494px;top:3px;width:112px;height:14px;background:#fff;border:1px solid #ccc;font-size:6px;color:#999;padding:3px 0 0 5px}
.search svg{position:absolute;right:3px;top:2px}

.header{left:0;top:20px;width:680px;height:41px;background:linear-gradient(#fff,#eee)}
.logo{left:74px;top:7px;display:flex;align-items:center;gap:5px}
.logo .mark{width:26px;height:26px;background:#555}
.logo .name{font-size:15px;font-weight:700;color:#444}
.social{top:17px;height:11px;background:#e6e6e6;border:1px solid #bbb}
.join{left:514px;top:10px;width:91px;height:22px;background:var(--red);color:#fff;font-size:11px;font-weight:700;text-align:center;line-height:22px}

.nav{left:0;top:61px;width:680px;height:27px;background:var(--blue);display:flex;padding-left:74px;align-items:center}
.nav a{color:#fff;font-size:6.3px;font-weight:700;text-decoration:none;margin-right:14px}

.hero{left:0;top:88px;width:680px;height:282px;background:linear-gradient(90deg,#c4dceb 0%,#d5e4ec 50%,#7d8a95 72%,#5b6670 82%,#a9c3d3 100%)}
.hero h1{left:78px;top:66px;font-size:23px;line-height:24px;font-weight:700;color:var(--ink)}
.hero .sub{left:78px;top:125px;width:300px;font-size:12.5px;line-height:15px;font-weight:700;color:#222}
.btn-enter{left:79px;top:199px;width:132px;height:44px;background:linear-gradient(var(--blue),var(--blue-dark));color:#fff;text-align:center;font-weight:700;font-size:18px;padding-top:6px}
.btn-enter small{display:block;font-size:7px;font-weight:400}
.btn-online{left:222px;top:199px;width:132px;height:44px;background:var(--red);color:#fff;display:flex;align-items:center;gap:6px;padding-left:12px}
.btn-online .t{line-height:16px;font-size:14px}
.btn-online .t b{display:block;font-size:19px}
.livehelp{left:658px;top:195px;width:22px;height:72px;background:var(--orange);color:#fff;font-size:8px;font-weight:700;writing-mode:vertical-rl;transform:rotate(180deg);text-align:center;line-height:22px}

.newbie{left:0;top:370px;width:680px;height:42px;background:var(--dark-band)}
.newbie p{position:absolute;left:75px;top:14px;font-family:"Noto Serif",Georgia,serif;font-style:italic;color:#fff;font-size:10px;white-space:nowrap;letter-spacing:-0.1px}
.newbie .click{left:521px;top:7px;width:84px;height:27px;background:linear-gradient(#eee,#bbb);color:#222;font-size:12px;text-align:center;line-height:27px}

.signal{left:0;top:412px;width:680px;height:36px;background:var(--grey-band);color:#fff}
.signal h2{position:absolute;left:74px;top:10px;font-size:15px;font-weight:700}
.signal .info{right:74px;top:13px;font-size:8px;font-weight:700;word-spacing:1px}

.letter{left:0;top:448px;width:680px;height:260px;background:var(--page)}
.letter .body{left:73px;top:13px;width:535px;font-size:7.6px;line-height:12px;color:#555}
.letter .body p{margin-bottom:8.5px}
.sig{left:73px;top:183px;width:62px;height:34px;background:linear-gradient(90deg,#ddd,#eee)}
.letter .signed{left:73px;top:226px;font-size:7.6px;color:#444}

.cols{left:0;top:708px;width:680px;height:200px}
.col{top:18px;width:170px}
.col h3{font-size:11px;font-weight:700;color:#222;margin-bottom:10px}
.col h3 span{color:var(--link)}
.col p{font-size:7.3px;line-height:11px;color:#555}
.col .date{color:var(--link);font-size:7.3px}
.col .item{padding-bottom:8px;margin-bottom:8px;border-bottom:1px solid #e5e5e5}
.col .item:last-child{border:none}
.divider{top:10px;width:1px;height:195px;background:#e5e5e5}
.news h4{font-size:8px;font-weight:700;color:#222;margin-bottom:8px}
.news .more{color:var(--link);font-size:7.3px}
.quote{font-size:7.3px;line-height:11px;color:#555}
.quote .by{color:var(--link);text-align:right;margin:10px 0 14px}
.rule{left:74px;top:927px;width:532px;height:1px;background:#e5e5e5}

.thumb{left:74px;top:950px;width:161px;height:112px;background:linear-gradient(#333 0 14px,#e8edf0 14px);border:1px solid #ccc}
.tabs{left:258px;top:944px;display:flex;gap:3px}
.tab{height:22px;padding:0 7px;background:#d9d9d9;font-size:8.5px;font-weight:700;color:#222;line-height:22px}
.tab.active{background:#3b86c6;color:#fff}
.panel{left:258px;top:966px;width:348px;height:98px;background:#f1f1f1;padding:12px 15px;font-size:7.3px;line-height:11px;color:#444}

.footer{left:0;top:1100px;width:680px;height:30px;background:var(--footer);color:#fff;font-size:7px}
.footer .links{left:74px;top:11px}
.footer .copy{right:74px;top:11px}
.disclaimer{left:0;top:1130px;width:680px;height:70px;background:#dcdcdc}
.disclaimer p{position:absolute;left:74px;top:9px;width:532px;font-size:5.4px;line-height:8.6px;color:#666}
</style>
</head>
<body>

<div class="abs topbar">
  <span class="abs item addr">48, Harbor Lane, Westfield, 512 Country
    <svg width="7" height="10" viewBox="0 0 7 10"><path d="M3.5 0C1.6 0 0 1.5 0 3.4 0 6 3.5 10 3.5 10S7 6 7 3.4C7 1.5 5.4 0 3.5 0z" fill="#888"/><circle cx="3.5" cy="3.4" r="1.2" fill="#ececec"/></svg>
  </span>
  <span class="abs item phone">Call us directly: (045) 731. 5820. 6472
    <svg width="9" height="10" viewBox="0 0 9 10"><rect x="1" y="0" width="7" height="10" rx="1" fill="#888"/><rect x="2" y="1.5" width="5" height="6" fill="#ececec"/></svg>
  </span>
  <div class="abs search">ENTER YOUR SEARCH...
    <svg width="9" height="9" viewBox="0 0 9 9"><circle cx="3.5" cy="3.5" r="2.5" fill="none" stroke="#888" stroke-width="1.2"/><path d="M5.5 5.5 8.5 8.5" stroke="#888" stroke-width="1.4"/></svg>
  </div>
</div>

<div class="abs header">
  <div class="abs logo"><span class="mark"></span><span class="name">BrightCoinDesk.info</span></div>
  <span class="abs social" style="left:428px;width:40px"></span>
  <span class="abs social" style="left:472px;width:16px"></span>
  <span class="abs social" style="left:492px;width:14px"></span>
  <div class="abs join">JOIN US FREE!</div>
</div>

<nav class="abs nav">
  <a>ENTER TRADING ROOM</a><a>FORUM</a><a>CONTROL PANEL</a><a>FOREX ADVICE</a><a>LIVE FOREX TRADING SIGNALS</a><a>BROKER REVIEWS</a><a>BECOME A TEAM TRADER</a><a>CONTACT US</a>
</nav>

<section class="abs hero" role="img" aria-label="Photo of a business man in a suit, arms crossed, standing among glass office towers under a pale sky">
  <h1 class="abs">FOLLOW<br>PROFESSIONAL TRADERS</h1>
  <p class="abs sub">Did you know you can copy trades automatically into your account using our special software?</p>
  <div class="abs btn-enter">ENTER NOW<small>(It's Free)</small></div>
  <div class="abs btn-online">
    <svg width="20" height="22" viewBox="0 0 20 22"><circle cx="10" cy="6" r="5" fill="#fff"/><path d="M0 22c0-7 4-9 10-9s10 2 10 9z" fill="#fff"/></svg>
    <span class="t">CURRENTLY<b>ONLINE</b></span>
  </div>
</section>
<div class="abs livehelp">LIVE HELP</div>

<div class="abs newbie">
  <p>Are you a total Newbie? Let us show you how to get start trading forex profitably today!</p>
  <div class="abs click">Click Here &#8250;</div>
</div>

<div class="abs signal">
  <h2>LATEST SIGNAL</h2>
  <span class="abs info">BUY - EURUSD &nbsp; Open Price: 1.3269 &nbsp;&nbsp; 2 hours ago</span>
</div>

<section class="abs letter">
  <div class="abs body">
    <p>My name is Reid Castellan and I'm the owner and founder of BrightCoinDesk.info. I created this site to reach out to all the retail forex traders in the world who are struggling to trade profitably.</p>
    <p>Here we give you the opportunity to connect with full time, professional forex traders and copy their signals inside our free forex trading room.</p>
    <p>I have extensive experience trading the forex market, however my true passion lies in building relationships with other talented and experienced traders across the globe and then benefiting from the profitable trading opportunities they identify by copying their trades.</p>
    <p>I make money by following forex traders who have the time, knowledge and skills needed to battle the market each day, and I share this opportunity with our members through the free forex trading room and automated forex signal copier.</p>
    <p>Please drop into the trading room so I can give you a tour and show you how you can make money following our team of forex traders.</p>
    <p>Sincerely</p>
  </div>
  <div class="abs sig" role="img" aria-label="Handwritten signature of the founder"></div>
  <span class="abs signed">Reid Castellan, BrightCoinDesk.info Founder</span>
</section>

<section class="abs cols">
  <div class="abs col" style="left:74px">
    <h3>Live <span>Updates</span></h3>
    <div class="item"><p>TQ Overdrive is continuing to dominate. Make sure you sign up soon if you want to follow this amazing trader. Subs cut off at 500!</p><span class="date">10 days ago</span></div>
    <div class="item"><p>Do you need a forex VPS? Check out our sister business! http://bcd.li/k7Rm2Pq</p><span class="date">27 days ago</span></div>
    <div class="item"><p>We have a new forum! Drop in to discuss anything and everything forex related. http://bcd.li/w3Hx9Ne</p><span class="date">28 days ago</span></div>
  </div>
  <div class="abs divider" style="left:247px"></div>
  <div class="abs col news" style="left:259px">
    <h3>Latest <span>News</span></h3>
    <h4>Watch Me Turn $30k into $300k!</h4>
    <p>I'm using $30k of my own funds to follow the signals at BrightCoinDesk.info to show everyone how easy it is to make passive income from forex with our help.</p>
    <p style="margin-top:11px">Follow my journey through a weekly update video on my VidStream Chanel.</p>
    <p class="more" style="margin-top:14px">Reid's Forex Journey To $300k!</p>
  </div>
  <div class="abs divider" style="left:432px"></div>
  <div class="abs col quote" style="left:446px;width:160px">
    <h3>Client's <span>Speak</span></h3>
    <p>“ I just bought a new TV and Dishwasher with the money I've made from this site. I couldn't have done it without you, thanks guys! ”</p>
    <p class="by">- Dunmore - Australia</p>
    <p style="border-top:1px solid #e5e5e5;padding-top:10px">I am following a few of the traders on the trade copier and in the past week I have grown my $800 account into $1,700!</p>
    <p class="by">- Tobin - Brisbane, Australia</p>
  </div>
</section>
<div class="abs rule"></div>

<div class="abs thumb" role="img" aria-label="Video preview showing the trading room screen with a play button"></div>
<div class="abs tabs">
  <span class="tab">Who Are We?</span><span class="tab">How Do We Do It?</span><span class="tab active">Is It Free?</span>
</div>
<div class="abs panel">YES! The trading signals are displayed live within the Forex Trading Room completely free of charge. You will also have the opportunity to discuss trade opportunities with our professional Team Traders in real time. We also provide trading activity from several third party signal providers and commercial EA's. Every forex strategy, signal and EA used on this site has a full REAL MONEY history available for review.</div>

<footer class="abs footer">
  <span class="abs links">Homepage | Trade Room History | Terms &amp; Conditions | Sitemap</span>
  <span class="abs copy">Copyright © 2013BrightCoinDesk.info. All Rights Reserved.</span>
</footer>
<div class="abs disclaimer">
  <p>Caution:Trading involves the possibility of financial loss. Only trade with money that you are prepared to lose, you must recognise that for factors outside your control you may lose all of the money in your trading account. Many forex brokers also hold you liable for losses that exceed your trading capital. So you may stand to lose more money than is in your account. BrightCoinDesk.info takes not responsibility for loss incurred as a result of our trading signals. By signing up as a member you acknowledge that we are not providing financial advice and that you are making a the decision to copy our trades on your own account. We have no knowledge on the level of money you are trading with or the level of risk you are taking with each trade. You must make your own financial decisions, we take no responsibility for money made or lost as a result of our signals or advice on forex related products on this website.</p>
</div>

</body>
</html>
```